New design for our thank you cards *

We need Thank You card designs for our mortgage broking company "Copperleaf Lending". We have an existing design and need a revamp of these. We are a boutique broking firm and would like "thank you" cards to send to our clients who refer new clients.

We are a referral-based business, our success and longevity is inextricably linked to the advice and service we provide our clients and referral partners.

Industry/Entity Type

Mortgage Brokerage

Colors
0792cd
0255a3
3176b5
33a6d7
85acd3
85cae6
cee9f5
cedeed
ffffff

Requirements
Must have
• our logo on the front 7 thank you & print on the back

```html
<!DOCTYPE html>
<html lang="en">
<head>
<meta charset="utf-8">
<title>Copperleaf Lending – Thank You Card</title>
<link href="https://fonts.googleapis.com/css2?family=Oswald:wght@300;400&family=Yellowtail&display=swap" rel="stylesheet">
<style>
  :root {
    --brand-deep: #0255a3;
    --brand-mid: #3176b5;
    --brand-bright: #0792cd;
    --brand-sky: #33a6d7;
    --brand-pale: #85cae6;
    --paper: #ffffff;
    --ink: #1a1a1a;
  }
  html, body {
    margin: 0;
    padding: 0;
    width: 849px;
    height: 1200px;
    overflow: hidden;
    background: var(--paper);
  }
  .sheet {
    position: relative;
    width: 849px;
    height: 1200px;
  }
  /* Front of card */
  .card-front {
    position: absolute;
    left: 0; top: 0;
    width: 849px; height: 600px;
    background: var(--brand-deep);
  }
  .card-front__panel {
    position: absolute;
    left: 50px; top: 33px;
    width: 748px; height: 529px;
    background: var(--paper);
    overflow: hidden;
  }
  .card-front__rule {
    position: absolute;
    left: 11px; top: 12px;
    width: 722px; height: 502px;
    border: 2px solid var(--brand-deep);
  }
  .bird-art {
    position: absolute;
    left: 70px; top: 61px;
    width: 217px; height: 192px;
    border-radius: 60% 40% 50% 30% / 50% 40% 60% 50%;
    background: linear-gradient(160deg, var(--brand-bright) 0%, var(--brand-sky) 45%, var(--brand-pale) 100%);
    opacity: 0.9;
  }
  .greeting-type {
    position: absolute;
    left: 0; top: 0;
    width: 748px; height: 529px;
  }
  .greeting {
    font-family: 'Yellowtail', cursive;
    font-size: 190px;
    fill: var(--brand-deep);
  }
  .greeting__sub {
    font-family: 'Oswald', sans-serif;
    font-weight: 300;
    font-size: 54px;
    fill: var(--ink);
  }
  /* Back of card */
  .card-back {
    position: absolute;
    left: 51px; top: 650px;
    width: 745px; height: 518px;
    border: 2px solid var(--brand-deep);
  }
  .brand {
    position: absolute;
    left: 168px; top: 167px;
    display: flex;
    align-items: center;
    gap: 22px;
  }
  .brand__mark {
    width: 120px; height: 120px;
    background: var(--brand-mid);
  }
  .brand__name {
    font-family: 'Oswald', sans-serif;
    font-weight: 400;
    font-size: 44px;
    line-height: 1.05;
    color: var(--ink);
    text-transform: uppercase;
    white-space: nowrap;
  }
  .brand__line { display: block; }
  .brand__line--top { letter-spacing: 3px; }
  .brand__line--bottom { letter-spacing: 14px; }
</style>
</head>
<body>
  <div class="sheet">
    <section class="card-front">
      <div class="card-front__panel">
        <div class="card-front__rule"></div>
        <div class="bird-art" role="img" aria-label="Illustration of a blue bird perched above the greeting"></div>
        <svg class="greeting-type" viewBox="0 0 748 529" aria-label="Thank You For Your Business">
          <text class="greeting" x="194" y="314" textLength="461" lengthAdjust="spacingAndGlyphs">Thank You</text>
          <text class="greeting__sub" x="201" y="374" textLength="322" lengthAdjust="spacingAndGlyphs">For Your Business</text>
        </svg>
      </div>
    </section>
    <section class="card-back">
      <div class="brand">
        <span class="brand__mark"></span>
        <span class="brand__name">
          <span class="brand__line brand__line--top">Copperleaf</span>
          <span class="brand__line brand__line--bottom">Lending</span>
        </span>
      </div>
    </section>
  </div>
</body>
</html>
```